Personal Blog

The wordpress blog style and layout should be similar to http://www.danholtmere.com

homepage: my photo, list of things, call to action then 3 boxes (The Blog, The Book and podcast)

Other pages: About us, Blog, Consulting, Contact

Target Market(s)

Web Marketing Consultant

Industry/Entity Type

Consulting

Colors
3277b5
33a6d7
f04a50
f68e4e
33b7a4

```html
<!DOCTYPE html>
<html lang="en">
<head>
<meta charset="utf-8">
<title>Karim Haddadi</title>
<link href="https://fonts.googleapis.com/css2?family=Dosis:wght@400;500;600;700&family=Arimo:wght@400;700&display=swap" rel="stylesheet">
<style>
:root{
  --teal:#33b7a4;
  --teal-bright:#2fd1bd;
  --teal-deep:#128a77;
  --dark:#1b2628;
  --ink:#222;
  --text:#333;
  --grey:#7d7d7d;
  --line:#d8dcdc;
  --paper:#eef3f3;
  --white:#fff;
}
*{margin:0;padding:0;box-sizing:border-box}
html,body{width:1200px;height:2204px;overflow:hidden}
body{background:var(--paper);font-family:'Arimo',Arial,sans-serif;color:var(--text);position:relative}
.heading{font-family:'Dosis',sans-serif}

.site-header{position:absolute;left:0;top:0;width:1200px;height:150px;background:linear-gradient(180deg,#2a3a3c,var(--dark))}
.brand{position:absolute;left:58px;top:62px;font-family:'Dosis',sans-serif;font-weight:600;font-size:44px;color:var(--white)}
.nav{position:absolute;right:60px;top:80px;display:flex;gap:26px;font-family:'Dosis',sans-serif;font-weight:500;font-size:22px;color:var(--white)}
.nav .active{color:var(--teal-bright)}
.header-band{position:absolute;left:0;top:150px;width:1200px;height:36px;background:linear-gradient(90deg,var(--teal),var(--teal-bright) 50%,var(--teal))}

.hero{position:absolute;left:0;top:186px;width:1200px;height:404px;background:linear-gradient(180deg,#f3f7f7,#e7eded)}
.hero-title{position:absolute;left:55px;top:35px;width:1100px;font-family:'Dosis',sans-serif;font-weight:500;font-size:42px;line-height:56px;color:var(--teal)}
.hero-title b{color:var(--ink);font-weight:500}
.topics{position:absolute;left:58px;top:150px;list-style:none;font-size:21px;color:var(--ink)}
.topics li{height:42px}
.topics li::before{content:"›";color:var(--teal);font-weight:700;margin-right:14px}
.hero-photo{position:absolute;left:618px;top:110px;width:530px;height:294px;background:linear-gradient(90deg,#c9cfd2,#e2e6ea 40%,#b7c3d3);border-radius:4px}

.testimonial{position:absolute;left:0;top:590px;width:1200px;height:200px}
.quote-mark{position:absolute;font-family:'Dosis',sans-serif;font-size:80px;color:#c9d0d0;line-height:1}
.quote-text{position:absolute;left:100px;top:90px;width:990px;text-align:center;font-family:'Dosis',sans-serif;font-weight:500;font-size:25px;line-height:36px;color:var(--ink)}
.quote-by{position:absolute;right:105px;top:160px;font-size:17px;color:var(--teal)}

.feature{position:absolute;top:812px;width:354px;height:384px;background:var(--white);border:1px solid var(--line)}
.feature svg{position:absolute;left:102px;top:40px}
.feature h3{position:absolute;top:200px;width:100%;text-align:center;font-family:'Dosis',sans-serif;font-weight:600;font-size:31px;color:var(--ink)}
.feature.active h3{color:var(--teal)}
.feature p{position:absolute;left:34px;top:248px;width:286px;text-align:center;font-size:15.5px;line-height:22px}
.btn{position:absolute;display:inline-flex;align-items:center;gap:6px;height:28px;padding:0 14px;border-radius:14px;background:#d9dddd;font-size:15px;color:var(--text)}
.btn::after{content:"";width:11px;height:11px;border:1.5px solid currentColor;border-radius:50%}
.btn.solid{background:var(--teal-bright);color:var(--white)}
.btn.outline{background:var(--white);border:1.5px solid #444}
.btn.outline.teal{border-color:var(--teal);color:var(--teal)}
.feature .btn{left:50%;transform:translateX(-50%);bottom:-14px}

.section-title{position:absolute;left:47px;top:1252px;width:1106px;height:40px}
.section-title::before,.section-title::after{content:"";position:absolute;top:19px;width:400px;height:2px;background:var(--line)}
.section-title::before{left:0}.section-title::after{right:0}
.section-title span{position:absolute;left:0;width:100%;text-align:center;font-family:'Dosis',sans-serif;font-weight:700;font-size:29px;color:var(--ink)}

.post{position:absolute;top:1330px;width:258px;height:446px;background:var(--white);border:1px solid var(--line)}
.post.active{border:2px solid var(--teal-bright)}
.post-media{position:absolute;left:4px;top:4px;right:4px;height:190px}
.post h4{position:absolute;left:20px;top:212px;width:225px;font-family:'Dosis',sans-serif;font-weight:600;font-size:22px;line-height:26px;color:var(--ink)}
.post.active h4{color:var(--teal)}
.post p{position:absolute;left:20px;top:300px;width:222px;font-size:14px;line-height:20px}
.post .btn{left:20px;top:384px}

.site-footer{position:absolute;left:0;top:1866px;width:1200px;height:290px;background:linear-gradient(135deg,#0fa08a,var(--teal-bright) 55%,var(--teal-deep))}
.col{position:absolute;top:50px;color:var(--white)}
.col h5{font-family:'Dosis',sans-serif;font-weight:700;font-size:29px;margin-bottom:20px}
.col p{font-size:15px;line-height:20px;margin-bottom:10px}
.field{width:340px;height:42px;background:var(--white);border-radius:3px;margin-bottom:18px;color:#333;font-size:15px;line-height:42px;padding-left:12px}
.join{width:340px;height:46px;background:var(--dark);color:var(--white);font-family:'Dosis',sans-serif;font-weight:700;font-size:28px;text-align:center;line-height:46px;border-radius:3px}
.socials{display:flex;gap:18px}
.social{width:56px;height:56px;background:var(--white);color:var(--teal-deep);font-family:'Dosis',sans-serif;font-weight:700;font-size:16px;display:flex;align-items:center;justify-content:center;border-radius:4px}
.or{text-align:center;font-size:16px;margin-top:18px;width:292px;line-height:24px}
.or a{color:var(--dark);text-decoration:none}

.legal{position:absolute;left:0;top:2156px;width:1200px;height:48px;background:var(--white);text-align:center;line-height:48px;font-size:15px;color:var(--ink)}
.legal a{color:var(--teal);text-decoration:none}
</style>
</head>
<body>
<header class="site-header">
  <div class="brand">Karim Haddadi</div>
  <nav class="nav"><span class="active">ABOUT</span><span>BLOG</span><span>CONSULTING</span><span>RESOURCES</span><span>BOOK</span><span>CONTACT</span></nav>
</header>
<div class="header-band"></div>

<section class="hero">
  <h1 class="hero-title">Test go here and <b>Product Management,</b> text here <b>Online Marketing,</b><br>to learn these topics:</h1>
  <ul class="topics">
    <li>Product Management</li><li>Customer Development</li><li>Digital Marketing</li><li>Branding &amp; Reputation</li><li>Entrepreneurship</li>
  </ul>
  <div class="hero-photo" role="img" aria-label="Portrait photo of the consultant in shirt and tie seated at a desk beside a computer monitor"></div>
</section>

<section class="testimonial">
  <div class="quote-mark" style="left:574px;top:20px">“</div>
  <div class="quote-mark" style="left:58px;top:85px;font-size:60px">“</div>
  <div class="quote-mark" style="right:52px;top:125px;font-size:60px">”</div>
  <p class="quote-text">"... I was blown away by his breadth of industry knowledge, the straight talking delivery and collaborative format. A highly recommended social media expert and thought leader..."</p>
  <div class="quote-by">-Owen de Marlo - Marketing</div>
</section>

<article class="feature active" style="left:47px">
  <svg width="150" height="150" viewBox="0 0 150 150"><circle cx="75" cy="75" r="72" fill="none" stroke="#2fd1bd" stroke-width="2"/><circle cx="75" cy="75" r="62" fill="#2fd1bd"/><ellipse cx="68" cy="68" rx="26" ry="20" fill="none" stroke="#fff" stroke-width="5"/><path d="M52 84 L46 98 L64 88" fill="none" stroke="#fff" stroke-width="5" stroke-linejoin="round"/><path d="M84 60 Q104 62 102 80 Q101 88 94 92 L100 104 L84 94" fill="none" stroke="#fff" stroke-width="5" stroke-linejoin="round"/></svg>
  <h3>The Blog</h3>
  <p>Lorem Ipsum is simply dummy text of the printing &amp; typesetting industry. Lorem Ipsum has been industry's standard dummy text ever since the 15000s.</p>
  <span class="btn solid">Read More</span>
</article>
<article class="feature" style="left:423px">
  <svg width="150" height="150" viewBox="0 0 150 150"><circle cx="75" cy="75" r="72" fill="none" stroke="#8a8a8a" stroke-width="2"/><circle cx="75" cy="75" r="62" fill="#7d7d7d"/><rect x="54" y="46" width="42" height="56" rx="4" fill="#fff"/><rect x="60" y="46" width="4" height="56" fill="#7d7d7d"/></svg>
  <h3>The Book</h3>
  <p>Lorem Ipsum is simply dummy text of the printing &amp; typesetting industry. Lorem Ipsum has been industry's standard dummy text ever since the 15000s.</p>
  <span class="btn">Read More</span>
</article>
<article class="feature" style="left:800px">
  <svg width="150" height="150" viewBox="0 0 150 150"><circle cx="75" cy="75" r="72" fill="none" stroke="#8a8a8a" stroke-width="2"/><circle cx="75" cy="75" r="62" fill="#7d7d7d"/><circle cx="84" cy="60" r="13" fill="#fff"/><path d="M60 100 Q62 78 84 78 Q106 78 108 100 Z" fill="#fff"/><circle cx="62" cy="66" r="10" fill="#fff"/><path d="M42 100 Q44 82 62 82 Q70 82 74 86 Q62 92 60 100 Z" fill="#fff"/></svg>
  <h3>Consulting</h3>
  <p>Lorem Ipsum is simply dummy text of the printing &amp; typesetting industry. Lorem Ipsum has been industry's standard dummy text ever since the 15000s.</p>
  <span class="btn">Read More</span>
</article>

<div class="section-title"><span>‹ RECENT POSTS ›</span></div>

<article class="post active" style="left:47px">
  <div class="post-media" role="img" aria-label="Photo of a team working around a wooden table with laptops" style="background:linear-gradient(135deg,#8a5a36,#c9a27a 50%,#5b4434)"></div>
  <h4>Yet Another Video Post Format With Embedded Media</h4>
  <p>Lorem Ipsum is simply dummy text of the printing &amp; typesetting industry. Lorem Ipsum has ...</p>
  <span class="btn outline teal">Read More</span>
</article>
<article class="post" style="left:330px">
  <div class="post-media" role="img" aria-label="Photo of business people in suits applauding" style="background:linear-gradient(135deg,#f2f2f2,#3b3f48 55%,#e6e6e6)"></div>
  <h4>Yet Another Video Post Format With Embedded Media</h4>
  <p>Lorem Ipsum is simply dummy text of the printing &amp; typesetting industry. Lorem Ipsum has ...</p>
  <span class="btn outline">Read More</span>
</article>
<article class="post" style="left:613px">
  <div class="post-media" role="img" aria-label="Photo of a hand touching a digital interface screen" style="background:linear-gradient(135deg,#1e2730,#6d7c8b 50%,#2a333c)"></div>
  <h4>Yet Another Video Post Format With Embedded Media</h4>
  <p>Lorem Ipsum is simply dummy text of the printing &amp; typesetting industry. Lorem Ipsum has ...</p>
  <span class="btn outline">Read More</span>
</article>
<article class="post" style="left:895px">
  <div class="post-media" role="img" aria-label="Photo of hands typing on a keyboard next to a desk phone" style="background:linear-gradient(135deg,#efe9e4,#b8a596 50%,#4b4f55)"></div>
  <h4>Yet Another Video Post Format With Embedded Media</h4>
  <p>Lorem Ipsum is simply dummy text of the printing &amp; typesetting industry. Lorem Ipsum has ...</p>
  <span class="btn outline">Read More</span>
</article>

<footer class="site-footer">
  <div class="col" style="left:47px;width:330px">
    <h5>ENTREPRENEUR, SPEAKER,</h5>
    <p>Lorem Ipsum is simply dummy text of the printing &amp; typesetting industry. Lorem Ipsum has been industry's standard dummy text ever since the 15000s.</p>
    <p>Lorem Ipsum is simply dummy text of the printing &amp; typesetting industry.</p>
  </div>
  <div class="col" style="left:423px">
    <h5>JOIN MY NEW BUSINESS</h5>
    <div class="field">Enter your name...</div>
    <div class="field">Enter your email...</div>
    <div class="join">JOIN FOR FREE!</div>
  </div>
  <div class="col" style="left:800px">
    <h5>CONNECT WITH ME</h5>
    <div class="socials"><span class="social">Pal</span><span class="social">Chirp</span><span class="social">Feed</span><span class="social">Vid</span></div>
    <p class="or">OR<br>Connect with via <a>email</a></p>
  </div>
</footer>
<div class="legal">© 2014 K. Haddadi <a>www.karimhaddadi.com</a> | All Right Reserved.</div>
</body>
</html>
```